Bright Owl Learning Centre website redesign

Our website (which we have only just converted to wordpress) is just not good enough for my liking. Our centre offers classes for babies aged from 6 months to 7 years old in the middle east. Whilst our program is formal in the way that the practise deals with learning in hemispheres of the brain - the site should look more fun and a bit more approachable and attractive to families.
I like the site www.tinyparade.example or www.plumvalley.example from this region - I like the way that you land on home page with images and a quote rather than all this information coming at you and you not knowing where to click.
I want a fun and appealing site that features info about the program, class timetable, shop, news and events, gallery, blog posts etc…
I am really open to a complete redesign and just want something that looks professional but is fun and gets the information out quickly! Please look at www.brightowl.example for current site design

```html
<!DOCTYPE html>
<html lang="en">
<head>
<meta charset="utf-8">
<title>Bright Owl Learning Centre</title>
<link rel="stylesheet" href="https://fonts.googleapis.com/css2?family=Fredoka+One&family=Ubuntu:wght@400;500;700&display=swap">
<style>
:root{
  --page:#f5f5f3;
  --white:#ffffff;
  --ink:#333333;
  --muted:#666666;
  --orange:#f39a2c;
  --blue:#3498db;
  --yellow:#fdd542;
  --green:#65a82c;
  --pink:#e9508a;
  --pink-soft:#f6b4cb;
  --red:#e8453c;
  --coral:#f26a5b;
  --heading:"Fredoka One", "Ubuntu", sans-serif;
  --body:"Ubuntu", sans-serif;
}
*{box-sizing:border-box;margin:0;padding:0}
html,body{width:1200px;height:3372px;overflow:hidden}
body{position:relative;background:var(--page);font-family:var(--body);color:var(--ink)}
.abs{position:absolute}
.page{position:absolute;left:130px;top:0;width:940px;height:3000px;background:var(--white)}
.brand{position:absolute;left:146px;top:18px;display:flex;align-items:center;gap:10px}
.brand-dot{width:40px;height:40px;border-radius:50%;background:var(--orange)}
.brand-name{font-family:var(--body);font-weight:700;font-size:24px;color:var(--blue)}
.social{display:flex;gap:12px}
.social span{display:block;width:28px;height:28px;border-radius:50%;background:var(--green)}
.top-links{position:absolute;left:480px;top:88px;display:flex;gap:18px;font-size:13px;color:var(--muted)}
.search{position:absolute;left:836px;top:84px;width:180px;height:24px;border:1px solid #ccc;font-size:11px;color:#aaa;padding:4px 8px}
.main-nav{position:absolute;left:130px;top:146px;width:940px;height:40px;background:var(--orange);display:flex;justify-content:space-around;align-items:center;font-family:var(--heading);font-size:15px;color:var(--white);letter-spacing:.5px}
.hero{position:absolute;left:130px;top:186px;width:940px;height:384px;background:linear-gradient(120deg,#d9b394 0%,#8fb6c8 45%,#6e9a5a 75%,#c9d7a0 100%)}
.hero-tags{position:absolute;right:134px;top:268px;display:flex;flex-direction:column;align-items:flex-end;gap:10px}
.hero-tags span{background:var(--green);color:var(--white);font-family:var(--heading);font-size:20px;padding:7px 12px;border:2px solid var(--white)}
.section{position:absolute;left:130px;width:940px}
.section-title{font-family:var(--heading);font-weight:400;font-size:36px;text-align:center}
.welcome{top:587px;height:332px;background:var(--blue);color:var(--white)}
.welcome .section-title{padding-top:28px;text-shadow:2px 2px 0 #1b5f8f}
.welcome-intro{position:absolute;left:25px;top:96px;width:420px;font-size:14px;line-height:19px}
.contact-line{position:absolute;left:25px;display:flex;align-items:center;gap:14px;font-size:24px}
.program{position:absolute;left:494px;top:114px}
.program h3{font-family:var(--heading);font-size:24px;font-weight:400;margin-bottom:14px}
.program li{list-style:none;display:flex;align-items:center;gap:12px;font-size:16px;height:44px}
.news{top:927px;height:408px;background:var(--yellow)}
.news .section-title{padding-top:18px;color:var(--ink);text-shadow:2px 2px 0 var(--white)}
.card{position:absolute;top:82px;width:281px;height:289px;background:var(--white)}
.card-img{height:100px;background:linear-gradient(135deg,#f3c9a8,#c8d9ea)}
.date{position:absolute;left:0;top:0;width:44px;background:var(--green);color:var(--white);text-align:center;font-size:18px;font-weight:700;line-height:22px;padding-top:2px}
.date small{display:block;font-size:9px;line-height:10px;padding-bottom:3px}
.comments{position:absolute;left:0;top:36px;width:44px;height:26px;background:var(--red);color:var(--white);font-size:13px;text-align:center;line-height:26px}
.card h4{font-size:15px;font-weight:500;line-height:19px;padding:18px 12px 8px}
.card p{font-size:12px;line-height:16px;color:var(--muted);padding:0 12px}
.btn{position:absolute;background:var(--orange);color:var(--white);font-size:12px;font-weight:700;padding:6px 12px}
.card .btn{left:105px;bottom:14px}
.staff{top:1349px;height:399px;background:linear-gradient(100deg,#f2dfe3,#e9e5ef 50%,#f4e2d4)}
.staff .section-title{padding-top:22px;color:var(--ink);text-shadow:2px 2px 0 var(--white)}
.member{position:absolute;top:92px;width:262px;height:276px;border:10px solid var(--pink-soft);background:linear-gradient(160deg,#e8c7b0,#b98d74)}
.member-name{position:absolute;left:20px;right:20px;bottom:46px;background:var(--pink);color:var(--white);text-align:center;font-size:16px;padding:4px}
.member-role{position:absolute;left:62px;right:62px;bottom:16px;background:var(--pink-soft);color:var(--white);text-align:center;font-size:14px;padding:3px}
.media{top:1765px;height:455px;background:var(--green);color:var(--white)}
.media h2{position:absolute;top:34px;font-family:var(--heading);font-weight:400;font-size:28px}
.video{position:absolute;left:25px;top:112px;width:266px;height:130px;background:#222;border:4px solid #111}
.video-screen{position:absolute;left:0;top:0;width:258px;height:100px;background:linear-gradient(135deg,#3b6e9e,#b5c6d8)}
.video-bar{position:absolute;left:8px;right:8px;bottom:8px;height:6px;background:#777}
.media p{position:absolute;font-size:13px;line-height:17px}
.star-name{position:absolute;left:484px;top:96px;font-size:22px;font-weight:500}
.star-photo{position:absolute;left:458px;top:150px;width:206px;height:206px;border-radius:50%;background:linear-gradient(135deg,#f0d3b8,#9bbfd9);border:8px solid var(--white)}
.gallery{top:2228px;height:503px;background:linear-gradient(120deg,#b99a86,#d8c4b0 50%,#a48672)}
.gallery .section-title{padding-top:28px;color:var(--white);text-shadow:2px 2px 0 #555}
.tile{position:absolute;width:212px;height:186px;border:3px solid var(--white);background:linear-gradient(135deg,#d8b7a0,#9cb7c9)}
.tile.feature{background:var(--yellow);display:flex;align-items:center;justify-content:center;gap:14px}
.tile.feature span{width:18px;height:18px;border-radius:50%;background:#444}
.press{top:2768px;height:190px}
.press .section-title{padding-top:10px;color:var(--ink)}
.press-row{position:absolute;left:60px;right:60px;top:122px;display:flex;justify-content:space-between;align-items:center;font-weight:700;font-size:20px;color:#222}
.press-row span{display:flex;align-items:center;gap:8px}
.press-row i{display:block;width:26px;height:26px;background:#222}
.footer{position:absolute;left:0;top:3001px;width:1200px;height:371px;background:var(--coral);color:var(--white)}
.footer h5{font-family:var(--heading);font-weight:400;font-size:22px;margin-bottom:14px}
.footer li{list-style:none;font-size:12px;line-height:16px;margin-bottom:8px;padding-left:12px;position:relative}
.footer li:before{content:"";position:absolute;left:0;top:6px;width:5px;height:5px;background:var(--white);border-radius:50%}
.footer p{font-size:12px;line-height:16px}
.flyer{position:absolute;left:857px;top:42px;width:216px;height:300px;background:var(--white);border:2px solid #ddd}
.flyer-art{position:absolute;left:16px;top:20px;width:184px;height:130px;background:linear-gradient(135deg,#f3b9a8,#f6e2d8)}
.flyer-text{position:absolute;left:16px;top:164px;width:184px;font-size:11px;line-height:14px;color:var(--ink)}
</style>
</head>
<body>
<div class="page"></div>

<header>
  <div class="brand"><span class="brand-dot"></span><span class="brand-name">Bright Owl</span></div>
  <div class="social abs" style="left:910px;top:20px"><span></span><span></span><span></span><span></span></div>
  <nav class="top-links"><span>The Program</span><span>Class Timetable</span><span>About</span><span>Contact</span></nav>
  <div class="search">Search</div>
</header>

<nav class="main-nav">
  <span>HOME</span><span>THE PROGRAM</span><span>CLASSES</span><span>MEDIA</span><span>LOCATION</span><span>BLOG</span><span>SHOP</span>
</nav>

<section class="hero" role="img" aria-label="Photo of a teacher and toddlers playing at a classroom table"></section>
<div class="hero-tags"><span>Speech Development</span><span>Focus &amp; Concentration</span><span>Sign Language</span><span>And More</span></div>

<section class="section welcome">
  <h1 class="section-title">Welcome to Bright Owl!</h1>
  <p class="welcome-intro">The Bright Owl Accelerated Learning Centre in Lakeside offers whole brain training for children from 6 months of age with the goal of promoting a balance in actively using both hemispheres of the brain equally throughout life.</p>
  <div class="contact-line" style="top:208px">
    <svg width="34" height="34" viewBox="0 0 24 24"><path d="M6.6 10.8a15 15 0 0 0 6.6 6.6l2.2-2.2c.3-.3.7-.4 1-.2 1.1.4 2.3.6 3.6.6.6 0 1 .4 1 1V20c0 .6-.4 1-1 1A17 17 0 0 1 3 4c0-.6.4-1 1-1h3.5c.6 0 1 .4 1 1 0 1.3.2 2.5.6 3.6.1.3 0 .7-.2 1z" fill="none" stroke="#fff" stroke-width="1.6"/></svg>
    <span>+000 5550 1234</span>
  </div>
  <div class="contact-line" style="top:258px">
    <svg width="34" height="26" viewBox="0 0 34 26"><rect x="1" y="1" width="32" height="24" rx="2" fill="none" stroke="#fff" stroke-width="2"/><path d="M1 2l16 13L33 2" fill="none" stroke="#fff" stroke-width="2"/></svg>
    <span>hello@brightowl.example</span>
  </div>
  <div class="program">
    <h3>The Program</h3>
    <ul>
      <li><svg width="22" height="22" viewBox="0 0 22 22"><circle cx="11" cy="11" r="9.5" fill="none" stroke="#fff" stroke-width="1.6"/><path d="M6.5 11.5l3 3 6-6" fill="none" stroke="#fff" stroke-width="1.8"/></svg>Bright Owl Program</li>
      <li><svg width="22" height="22" viewBox="0 0 22 22"><circle cx="11" cy="11" r="9.5" fill="none" stroke="#fff" stroke-width="1.6"/><path d="M6.5 11.5l3 3 6-6" fill="none" stroke="#fff" stroke-width="1.8"/></svg>The Science</li>
      <li><svg width="22" height="22" viewBox="0 0 22 22"><circle cx="11" cy="11" r="9.5" fill="none" stroke="#fff" stroke-width="1.6"/><path d="M6.5 11.5l3 3 6-6" fill="none" stroke="#fff" stroke-width="1.8"/></svg>What is Whole Brain Training?</li>
      <li><svg width="22" height="22" viewBox="0 0 22 22"><circle cx="11" cy="11" r="9.5" fill="none" stroke="#fff" stroke-width="1.6"/><path d="M6.5 11.5l3 3 6-6" fill="none" stroke="#fff" stroke-width="1.8"/></svg>Testimonials</li>
    </ul>
  </div>
</section>

<section class="section news">
  <h2 class="section-title">News And Events</h2>
  <article class="card" style="left:25px">
    <div class="card-img" role="img" aria-label="Photo of a smiling woman with a child"></div>
    <div class="date">09<small>Apr 2014</small></div><div class="comments">5</div>
    <h4>LaunchPad Monthly interviews our Director Mariam Hollis</h4>
    <p>Statistics about the brain are manifold and fascinating. Did you know that the energy used by the brain ...</p>
    <span class="btn">Read More</span>
  </article>
  <article class="card" style="left:320px">
    <div class="card-img" role="img" aria-label="Photo of children at a party with balloons"></div>
    <div class="date">10<small>Mar 2014</small></div><div class="comments">2</div>
    <h4>Club Marvella Magic Show for End of Term Party!</h4>
    <p>Abracadabra! It's the Bright Owl end of term party! Join us for a free show hosted by Club Marvella ...</p>
    <span class="btn">Read More</span>
  </article>
  <article class="card" style="left:615px">
    <div class="card-img" role="img" aria-label="Photo of a toddler with a gift box"></div>
    <div class="date">30<small>Mar 2014</small></div><div class="comments">4</div>
    <h4>Petal Box has landed at the Bright Owl Centre!</h4>
    <p>We're extremely proud to have teamed up with Petal Box this month! Petal Box is a great new product ...</p>
    <span class="btn">Read More</span>
  </article>
</section>

<section class="section staff">
  <h2 class="section-title">Meet the Staff</h2>
  <div class="member" style="left:25px" role="img" aria-label="Portrait of the founder">
    <div class="member-name">Mariam Hollis</div><div class="member-role">Founder</div>
  </div>
  <div class="member" style="left:334px" role="img" aria-label="Portrait of a teacher">
    <div class="member-name">Clara Denton</div><div class="member-role">Teacher</div>
  </div>
  <div class="member" style="left:653px" role="img" aria-label="Portrait of a teacher">
    <div class="member-name">Iris Callow</div><div class="member-role">Teacher</div>
  </div>
</section>

<section class="section media">
  <h2 style="left:25px">Bright Owl on Channel East</h2>
  <h2 style="left:522px">Star of the Month</h2>
  <div class="video">
    <div class="video-screen" role="img" aria-label="Still from a television interview in a studio"></div>
    <div class="video-bar"></div>
  </div>
  <p style="left:304px;top:110px;width:140px">Bright Owl's Director Mariam Hollis is interviewed on Studio Nine on the Channel East TV channel about the Accelerated Learning Program. She talks about brain</p>
  <p style="left:25px;top:262px;width:415px">training for 6 months up and how the key area of development takes place before 6 years of age, teaching parents and carers to have faith in their child's abilities and how the program can help with discovering new parenting styles and more.</p>
  <div class="star-name">Nora (5 years)</div>
  <div class="star-photo" role="img" aria-label="Photo of the star pupil of the month"></div>
  <p style="left:700px;top:148px;width:210px">Every month we will choose our unique Star of the Month from within the Bright Owl community. This could be a student, parent, carer or teacher that we feel has contributed great support, worked super hard or has shown high levels of ...</p>
  <span class="btn" style="left:797px;top:340px">Read More</span>
</section>

<section class="section gallery">
  <h2 class="section-title">Photo Gallery</h2>
  <div class="tile feature" style="left:25px;top:98px"><span></span><span></span><span></span></div>
  <div class="tile" style="left:244px;top:98px" role="img" aria-label="Photo of children building with blocks"></div>
  <div class="tile" style="left:466px;top:98px" role="img" aria-label="Photo of a toddler painting"></div>
  <div class="tile" style="left:690px;top:98px" role="img" aria-label="Photo of children on a play mat"></div>
  <div class="tile" style="left:25px;top:290px" role="img" aria-label="Photo of a class sitting in a circle"></div>
  <div class="tile" style="left:244px;top:290px" role="img" aria-label="Photo of a teacher reading to toddlers"></div>
  <div class="tile" style="left:466px;top:290px" role="img" aria-label="Photo of children in colourful costumes"></div>
  <div class="tile" style="left:690px;top:290px" role="img" aria-label="Photo of a child playing with a puzzle"></div>
</section>

<section class="section press">
  <h2 class="section-title">Who's talking about Bright Owl?</h2>
  <svg class="abs" style="left:16px;top:128px" width="18" height="28" viewBox="0 0 18 28"><path d="M18 0L0 14l18 14z" fill="#f2c11a"/></svg>
  <svg class="abs" style="left:906px;top:128px" width="18" height="28" viewBox="0 0 18 28"><path d="M0 0l18 14L0 28z" fill="#f2c11a"/></svg>
  <div class="press-row">
    <span><i style="border-radius:50%"></i>Radio 104</span>
    <span>Channel East</span>
    <span>Daily Seven</span>
    <span>The Gazette</span>
    <span><i></i>City Guide Kids</span>
  </div>
</section>

<footer class="footer">
  <div class="abs" style="left:132px;top:42px;width:250px">
    <h5>Recent Posts</h5>
    <ul>
      <li>LaunchPad Monthly interviews our Director Mariam Hollis</li>
      <li>Club Marvella Magic Show for End of Term Party!</li>
      <li>Hollow Pine's new Grandparents Frame</li>
      <li>Petal Box has landed at the Bright Owl Centre!</li>
      <li>Join us at our FREE City Guide Kids open day – 13th April!</li>
    </ul>
  </div>
  <div class="abs" style="left:421px;top:42px;width:150px">
    <h5>Archives</h5>
    <ul><li>April 2014</li><li>March 2014</li><li>February 2014</li><li>December 2013</li></ul>
    <h5 style="margin-top:20px">Categories</h5>
    <ul><li>Child Development</li><li>News &amp; Events</li></ul>
  </div>
  <div class="abs" style="left:582px;top:42px;width:250px">
    <h5>Contact US</h5>
    <p>Bright Owl Accelerated Learning Centre<br>Unit 5, Block 2, Garden Campus, Lakeside<br>(Located between the main gate and the east entrance)</p>
    <p style="margin-top:46px">© Bright Owl Accelerated Learning Centre. All Rights Reserved.</p>
    <div class="social" style="margin-top:18px"><span style="background:#fff"></span><span style="background:#fff"></span><span style="background:#fff"></span><span style="background:#fff"></span></div>
  </div>
  <div class="flyer">
    <div class="flyer-art" role="img" aria-label="Illustration of a child's head showing the brain"></div>
    <div class="flyer-text"><strong>Is your child left or right brained?</strong><br>Simple tests you can try at home with your little one this week.<br><br>How smart is your right foot?</div>
  </div>
</footer>
</body>
</html>
```